Graphic or Colorful Core Values Wall

I need artwork for an executive conference room wall. It is the blank space between the window and bookshelf (some photos have a blue 24x48 paper taped to the wall). I'm open to material options. The room has metal, wood, acrylic, black, silver, navy blue, saddle leather chairs, and a white conference table. There will be a sideboard/table below the artwork for balance. Not sure what that'll look like yet. You can see the mockups in the pdfs. You can read more about our heritage at bvtrx.com. <-- Feel free to use imagery from here if need be.

We have been around since 1929 so anything historical is fair game. We built the shell-shaped kestrel station in Winston-Salem, NC (only 1 remains today) However we have diversified greatly since then.

Target Market(s)

Executives

Font styles to use
Sans Serif
Other font styles liked:
• Century Gothic for the main font, "Since 1929" is in Jelytta

Requirements
Must have
• The artwork or graphic must include the following Core Values: do it because it is right treat customers, vendors, and fellow employees as we would like to be treated be financially responsible be better today than yesterday Vision: To be the best at what we choose to do as recognized by our co-workers, customers, and competitors. Mission: To expand and develop our company through strict adherence to our "Core Ideology." We will empower, train, and motivate "Harlow People" to strive for operational excellence.
Nice to have
• Owner likes color but the room doesn't have much color. Our logo has Red: #E10920 and Yellow: #FCBF15 in it
Should not have
• Look through our website and see how we use primary colors. We need to stay on brand as well as fit the room.

```html
<!DOCTYPE html>
<html lang="en">
<head>
<meta charset="utf-8">
<title>Core Values Wall Panel</title>
<link href="https://fonts.googleapis.com/css2?family=Great+Vibes&family=Jost:wght@500;600;700&display=swap" rel="stylesheet">
<style>
  :root {
    --page: #ffffff;
    --panel-light: #e6e8eb;
    --panel-mid: #d7dade;
    --band: #2b2b2c;
    --red: #e10920;
    --yellow: #fcbf15;
    --ink: #1d1d1f;
    --white: #ffffff;
    --dash: #3a3a3a;
  }
  * { margin: 0; padding: 0; box-sizing: border-box; }
  html, body { width: 835px; height: 1200px; overflow: hidden; background: var(--page); }
  .canvas { position: relative; width: 835px; height: 1200px; }
  .panel {
    position: absolute; left: 38px; top: 410px; width: 760px; height: 380px;
    background: var(--panel-light);
    box-shadow: 0 6px 18px rgba(0,0,0,.18);
    overflow: hidden;
    font-family: "Jost", sans-serif;
  }
  .world-map {
    position: absolute; left: 0; top: 60px; width: 760px; height: 194px;
    background: radial-gradient(ellipse at 50% 50%, #f1f2f4 0%, var(--panel-mid) 70%, var(--panel-light) 100%);
  }
  .since {
    position: absolute; left: 0; right: 0; top: 8px; text-align: center;
    font-family: "Great Vibes", cursive; font-size: 32px; color: var(--ink); line-height: 1;
  }
  .headline {
    position: absolute; left: 0; right: 0; top: 42px; text-align: center;
    font-weight: 700; font-size: 62px; line-height: 1; color: var(--red); letter-spacing: -1px;
  }
  .connectors { position: absolute; left: 0; top: 110px; }
  .value {
    position: absolute; top: 134px; width: 190px; margin-left: -95px; text-align: center;
  }
  .value-icon {
    width: 56px; height: 56px; margin: 0 auto; border-radius: 50%;
    background: var(--white); box-shadow: -6px 8px 12px rgba(0,0,0,.14);
    display: flex; align-items: center; justify-content: center;
  }
  .value-label {
    margin-top: 11px; font-weight: 600; font-size: 13px; line-height: 16px; color: var(--ink);
  }
  .statement-band {
    position: absolute; left: 0; top: 254px; width: 760px; height: 126px; background: var(--band);
  }
  .statement-title {
    position: absolute; top: 22px; font-weight: 700; line-height: .9; text-transform: uppercase;
  }
  .statement-title .lead { display: block; color: var(--yellow); font-size: 50px; letter-spacing: -1px; }
  .statement-title .word { display: block; color: var(--red); }
  .vision-title { left: 33px; }
  .vision-title .word { font-size: 32px; }
  .mission-title { left: 390px; top: 25px; }
  .mission-title .lead { font-size: 49px; }
  .mission-title .word { font-size: 26px; }
  .statement-text {
    position: absolute; color: var(--white); font-weight: 500; font-size: 11.3px; line-height: 14.5px;
  }
  .vision-text { left: 164px; top: 37px; width: 180px; }
  .mission-text { left: 514px; top: 22px; width: 230px; }
  .band-divider {
    position: absolute; left: 361px; top: 16px; height: 80px; border-left: 1px dashed #8a8a8a;
  }
</style>
</head>
<body>
<div class="canvas">
  <section class="panel">
    <div class="world-map" role="img" aria-label="Faint dotted world map spread behind the core values"></div>
    <div class="since">Since 1929</div>
    <h1 class="headline">CORE VALUES</h1>

    <svg class="connectors" width="760" height="24" viewBox="0 0 760 24" fill="none" stroke="var(--dash)" stroke-width="1" stroke-dasharray="3 2">
      <path d="M232 2 V12 H102 V24"/>
      <path d="M361 2 V12 H279 V24"/>
      <path d="M388 2 V12 H469 V24"/>
      <path d="M529 2 V12 H657 V24"/>
    </svg>

    <div class="value" style="left:102px">
      <div class="value-icon">
        <svg width="30" height="30" viewBox="0 0 30 30" fill="none" stroke="var(--ink)" stroke-width="1.4" stroke-linecap="round">
          <path d="M6 6 L24 24"/><path d="M4 9 a4 4 0 0 1 5-5"/><path d="M24 6 L8 22" stroke="var(--red)" stroke-width="2.4"/><path d="M26 4 L22 8"/><circle cx="23" cy="23" r="3"/>
        </svg>
      </div>
      <p class="value-label">Do it because<br>it is right</p>
    </div>
    <div class="value" style="left:282px">
      <div class="value-icon">
        <svg width="30" height="30" viewBox="0 0 30 30" fill="none" stroke-width="1.4" stroke-linecap="round">
          <path d="M15 15 C9 10 9 5 12 5 C14 5 15 7 15 7 C15 7 16 5 18 5 C21 5 21 10 15 15Z" stroke="var(--red)"/>
          <path d="M5 12 V20 L11 26" stroke="var(--ink)"/><path d="M25 12 V20 L19 26" stroke="var(--ink)"/>
        </svg>
      </div>
      <p class="value-label">Treat customers, vendors,<br>and fellow employees as<br>we would like to be treated</p>
    </div>
    <div class="value" style="left:469px">
      <div class="value-icon">
        <svg width="30" height="30" viewBox="0 0 30 30" fill="none" stroke-width="1.4" stroke-linecap="round">
          <circle cx="10" cy="8" r="4" stroke="var(--ink)"/>
          <path d="M14 14 L19 10 L22 12 L27 6" stroke="var(--red)"/>
          <path d="M3 22 L9 19 H17 L25 17 L14 25 H6" stroke="var(--ink)"/>
        </svg>
      </div>
      <p class="value-label" style="margin-top:13px">Be financially<br>responsible</p>
    </div>
    <div class="value" style="left:657px">
      <div class="value-icon">
        <svg width="30" height="30" viewBox="0 0 30 30" fill="none" stroke-width="1.4" stroke-linecap="round">
          <rect x="4" y="21" width="4" height="4" stroke="var(--red)"/>
          <rect x="10" y="18" width="4" height="7" stroke="var(--red)"/>
          <rect x="16" y="15" width="4" height="10" stroke="var(--red)"/>
          <rect x="22" y="12" width="4" height="13" stroke="var(--ink)"/>
          <path d="M5 16 L15 8 M11 8 H15 V12" stroke="var(--ink)"/>
        </svg>
      </div>
      <p class="value-label">Be better today<br>than yesterday</p>
    </div>

    <div class="statement-band">
      <h2 class="statement-title vision-title"><span class="lead">Our</span><span class="word">Vision</span></h2>
      <p class="statement-text vision-text">To be the best at what we choose to do as recognized by our co-workers, customers, and competitors.</p>
      <div class="band-divider"></div>
      <h2 class="statement-title mission-title"><span class="lead">Our</span><span class="word">Mission</span></h2>
      <p class="statement-text mission-text">To expand and develop our company through strict adherence to our "Core Ideology." We will empower, train, and motivate "Harlow People" to strive for operational excellence.</p>
    </div>
  </section>
</div>
</body>
</html>
```